New cosmetics company needs packaging design

We need a packaging design for our new cosmetics brand. We are looking for modern, sleek packaging such as black or white packaging with gold text. The packaging will be for boxes of different sizes for eye pencils, lipsticks, foundation etc. For example small long rectangle boxes, standing rectangle boxes and square boxes for products.
Attached is a pattern we were thinking to be used on the inside of the boxes and maybe some elements of this pattern on the outside of the boxes. This is not a strict requirement, we are happy to receive other ideas.
Our logo is a 5-letter word and we have a round symbol, which we'll be happy to send after seeing some designs.
Thank you.

```html
<!DOCTYPE html>
<html lang="en">
<head>
<meta charset="utf-8">
<title>LUVRA – Packaging</title>
<link rel="stylesheet" href="https://fonts.googleapis.com/css2?family=Cormorant+Garamond:wght@500&family=Jost:wght@400;500;700&display=swap">
<style>
  :root {
    --backdrop: #e4e4e4;
    --ink-black: #0c0c0c;
    --panel-black: #161616;
    --gold: #d9b45a;
    --gold-light: #f7de8a;
    --gold-deep: #a87a1c;
    --label-text: #e8d9b0;
  }
  * { box-sizing: border-box; margin: 0; padding: 0; }
  html, body { width: 1200px; height: 845px; overflow: hidden; }
  body {
    background: radial-gradient(ellipse at 50% 40%, #f2f2f2 0%, var(--backdrop) 70%);
    font-family: "Jost", sans-serif;
    position: relative;
  }
  .panel {
    position: absolute;
    background: linear-gradient(180deg, #1e1e1e 0%, var(--panel-black) 50%, var(--ink-black) 100%);
    display: flex;
    flex-direction: column;
    align-items: center;
    text-align: center;
    color: var(--label-text);
    overflow: hidden;
  }
  .gold-band {
    position: absolute; left: 0; right: 0; bottom: 0;
    background: linear-gradient(180deg, var(--gold-light) 0%, var(--gold) 45%, var(--gold-deep) 100%);
    color: var(--ink-black);
    font-weight: 500;
    display: flex; align-items: center; justify-content: center;
  }
  .brand-mark {
    width: 40px; height: 40px; border-radius: 50%;
    background: linear-gradient(135deg, var(--gold-light), var(--gold-deep));
  }
  .brand-name {
    font-family: "Jost", sans-serif;
    font-weight: 500;
    color: var(--gold);
    letter-spacing: 3px;
  }
  .product-name {
    font-family: "Cormorant Garamond", serif;
    font-weight: 500;
    color: var(--gold);
    line-height: 1.1;
  }
  .body-copy { font-size: 10px; line-height: 1.35; color: var(--label-text); }
  .cta {
    background: linear-gradient(180deg, var(--gold-light), var(--gold) 55%, var(--gold-deep));
    color: var(--ink-black);
    font-weight: 700;
    border-radius: 14px;
    padding: 3px 14px;
  }

  /* bottle label */
  .bottle-label { left: 250px; top: 170px; width: 190px; height: 500px; padding: 36px 14px 0; }
  .bottle-label .brand-mark { width: 44px; height: 44px; }
  .bottle-label .brand-name { font-size: 28px; margin-top: 8px; }
  .bottle-label .product-name { font-size: 34px; margin-top: 14px; }
  .bottle-label .body-copy { margin-top: 14px; font-size: 9px; }
  .bottle-label .cta { margin-top: 16px; font-size: 16px; }
  .bottle-label .fine-print { font-size: 8.5px; margin-top: 18px; }
  .bottle-label .gold-band { height: 40px; font-size: 14px; }

  /* box front */
  .box-front { left: 490px; top: 110px; width: 260px; height: 640px; padding: 56px 20px 0; }
  .box-front .brand-mark { width: 62px; height: 62px; }
  .box-front .brand-name { font-size: 40px; margin-top: 12px; }
  .box-front .product-name { font-size: 48px; margin-top: 40px; }
  .box-front .body-copy { margin-top: 26px; font-size: 10.5px; }
  .box-front .cta { margin-top: 42px; font-size: 19px; }
  .box-front .fine-print { font-size: 10.5px; margin-top: 22px; }
  .box-front .gold-band { height: 48px; font-size: 15px; }

  /* box side */
  .box-side {
    left: 750px; top: 110px; width: 180px; height: 640px; padding: 34px 16px 0;
    background: linear-gradient(180deg, #101010 0%, #0a0a0a 100%);
    border-left: 1px solid #2a2a2a;
  }
  .box-side .product-name { font-size: 26px; align-self: flex-start; text-align: left; }
  .box-side .body-copy { margin-top: 12px; font-size: 10px; text-align: justify; }
  .box-side .brand-mark { margin-top: 40px; width: 48px; height: 48px; }
  .box-side .brand-name { font-size: 28px; margin-top: 10px; }
  .box-side .fine-print { font-size: 8px; margin-top: 14px; }
  .box-side .gold-band { height: 48px; }
</style>
</head>
<body>

  <section class="panel bottle-label" aria-label="Bottle label">
    <div class="brand-mark"></div>
    <div class="brand-name">LUVRA</div>
    <h2 class="product-name">PRODUCT<br>NAME</h2>
    <p class="body-copy">Lorem ipsum dolor sit amet, consectetur adipisicing elit, sed do eiusmod tempor incididunt ut labore et dolore magna aliqua. Ut enim ad minim veniam, quis nostrud exercitation.</p>
    <span class="cta">TEXT HERE!</span>
    <p class="body-copy fine-print">Lorem ipsum dolor sit amet, consectetur.</p>
    <div class="gold-band">150 ml | 8.4 oz</div>
  </section>

  <section class="panel box-front" aria-label="Box front panel">
    <div class="brand-mark"></div>
    <div class="brand-name">LUVRA</div>
    <h1 class="product-name">PRODUCT<br>NAME</h1>
    <p class="body-copy">Lorem ipsum dolor sit amet, consectetur adipisicing elit, sed do eiusmod tempor incididunt ut labore et dolore magna aliqua. Ut enim ad minim veniam, quis nostrud exercitation.</p>
    <span class="cta">TEXT HERE!</span>
    <p class="body-copy fine-print">Lorem ipsum dolor sit amet,<br>consectetur adipisicing elit.</p>
    <div class="gold-band">150 ml | 8.4 oz</div>
  </section>

  <section class="panel box-side" aria-label="Box side panel">
    <h2 class="product-name">PRODUCT NAME</h2>
    <p class="body-copy">Lorem ipsum dolor sit amet, consectetur adipisicing elit, sed do eiusmod tempor incididunt ut labore et dolore magna aliqua. Ut enim ad minim veniam, quis nostrud exercitation. Lorem ipsum dolor sit amet, consectetur adipisicing elit, sed do eiusmod tempor incididunt ut labore et dolore magna aliqua. Ut enim ad minim veniam, quis nostrud exercitation. Lorem ipsum dolor sit amet, consectetur adipisicing elit, sed do eiusmod tempor incididunt ut labore et dolore magna aliqua. Ut enim ad minim veniam, quis nostrud exercitation. Lorem ipsum dolor sit amet, consectetur adipisicing elit, sed do eiusmod tempor incididunt ut labore et dolore magna aliqua. Ut enim ad minim veniam, quis nostrud exercitation.</p>
    <div class="brand-mark"></div>
    <div class="brand-name">LUVRA</div>
    <p class="body-copy fine-print">Lorem ipsum dolor sit amet, consectetur.</p>
    <div class="gold-band"></div>
  </section>

</body>
</html>
```